ashby paving works

Needs to have phone number 0412885107 and email marklowry@pavemail.com.au.
ABN 27613048852
name mark lowry

For all your concreting solutions
Excavation
Exposed & colour concrete
House & shed slabs
Driveways
Landing & steps

Contact Information for Business Card

ph 0412885107
email marklowry@pavemail.com.au.
ABN 27613048852
name mark lowry

```html
<!DOCTYPE html>
<html lang="en">
<head>
<meta charset="utf-8">
<title>Ashby Paving Works – Business Card</title>
<link href="https://fonts.googleapis.com/css2?family=Oswald:wght@300;400;600;700&display=swap" rel="stylesheet">
<style>
  :root {
    --backdrop: #e6e7e9;
    --card-white: #ffffff;
    --card-black: #000000;
    --orange: #f26a21;
    --slate: #6d6e70;
    --ink: #000000;
    --paper-text: #ffffff;
  }
  * { margin: 0; padding: 0; box-sizing: border-box; }
  html, body { width: 1200px; height: 1200px; overflow: hidden; }
  body {
    background: var(--backdrop);
    position: relative;
    font-family: "Oswald", sans-serif;
  }
  .card { position: absolute; overflow: hidden; }

  /* Front */
  .card-front { left: 242px; top: 154px; width: 715px; height: 419px; background: var(--card-white); }
  .brand { position: absolute; left: 40px; top: 30px; height: 95px; display: flex; align-items: center; }
  .brand-mark { width: 34px; height: 34px; background: var(--orange); margin-right: 44px; }
  .brand-rule { width: 2px; height: 95px; background: var(--orange); margin-right: 12px; }
  .brand-text { display: flex; flex-direction: column; }
  .brand-name { font-weight: 600; font-size: 22px; color: var(--orange); letter-spacing: 0.5px; line-height: 1.15; text-transform: uppercase; }
  .brand-phone { font-weight: 400; font-size: 15px; color: var(--orange); letter-spacing: 2px; line-height: 1.3; }

  .tab { position: absolute; top: 150px; width: 23px; height: 116px; }
  .tab-left { left: 0; background: var(--orange); border-radius: 0 23px 23px 0; }
  .tab-right { right: 0; background: var(--slate); border-radius: 23px 0 0 23px; }

  .person-name { position: absolute; left: 40px; top: 200px; font-weight: 700; font-size: 56px; line-height: 1; color: var(--ink); }

  .contact { position: absolute; left: 40px; top: 314px; display: grid; grid-template-columns: auto auto; }
  .contact-labels { color: var(--orange); font-weight: 300; font-size: 21px; line-height: 25px; padding-right: 4px; border-right: 2px solid var(--orange); }
  .contact-values { color: var(--ink); font-weight: 300; font-size: 23px; line-height: 25px; padding-left: 4px; }

  /* Back */
  .card-back { left: 246px; top: 633px; width: 709px; height: 417px; background: var(--card-black); }
  .tagline { position: absolute; left: 39px; top: 75px; font-weight: 600; font-size: 41px; line-height: 1; color: var(--orange); }
  .services { position: absolute; left: 39px; top: 127px; list-style: none; }
  .services li { display: flex; align-items: center; height: 42px; font-weight: 400; font-size: 29px; color: var(--paper-text); }
  .bullet { width: 14px; height: 14px; background: var(--orange); margin: 0 27px 0 6px; }
  .corner-block { position: absolute; right: -40px; bottom: -40px; width: 110px; height: 110px; background: #2d2a28; }
</style>
</head>
<body>
  <section class="card card-front" aria-label="Business card front">
    <div class="brand">
      <span class="brand-mark"></span>
      <span class="brand-rule"></span>
      <div class="brand-text">
        <span class="brand-name">Ashby Paving Works</span>
        <span class="brand-phone">0412885107</span>
      </div>
    </div>
    <span class="tab tab-left"></span>
    <span class="tab tab-right"></span>
    <h1 class="person-name">Mark Lowry</h1>
    <div class="contact">
      <div class="contact-labels">Ph.<br>Email<br>ABN</div>
      <div class="contact-values">0412885107<br>marklowry@pavemail.com.au.<br>27613048852</div>
    </div>
  </section>

  <section class="card card-back" aria-label="Business card back">
    <h2 class="tagline">For all concreting solutions</h2>
    <ul class="services">
      <li><span class="bullet"></span>Excavation</li>
      <li><span class="bullet"></span>Exposed &amp; Colour Concrete</li>
      <li><span class="bullet"></span>house &amp; Shed slabs</li>
      <li><span class="bullet"></span>Driveways</li>
      <li><span class="bullet"></span>Landing &amp; Steps</li>
    </ul>
    <span class="corner-block"></span>
  </section>
</body>
</html>
```